Copperleaf Motorized Shade Business Card

Hello, we've had our logo made. Now we are looking for a clean and cool looking business card. One side can just be the logo with any design elements that might look good with it. The other side will be Name, Phone Number and Email. There will not be an address on the card.

```html
<!DOCTYPE html>
<html lang="en">
<head>
<meta charset="utf-8">
<title>Copperleaf Motorized Shade – Business Card</title>
<link rel="stylesheet" href="https://fonts.googleapis.com/css2?family=Bebas+Neue&family=Open+Sans:wght@400&display=swap">
<style>
  :root {
    --backdrop: #9a9a9a;
    --paper: #f6f6f6;
    --navy: #1d4a86;
    --navy-deep: #153a6c;
    --sky: #22b3ea;
    --sun: #f4c02a;
    --ink: #555a60;
    --edge: #d86a10;
  }
  html, body {
    margin: 0;
    width: 1200px;
    height: 801px;
    overflow: hidden;
    background: var(--backdrop);
  }
  .sheet {
    position: relative;
    width: 1200px;
    height: 801px;
  }
  .card {
    position: absolute;
    top: 257px;
    width: 500px;
    height: 286px;
    box-sizing: border-box;
    border-bottom: 3px solid var(--edge);
    box-shadow: 0 14px 30px rgba(0,0,0,0.28);
    overflow: hidden;
  }
  .card--front {
    left: 70px;
    background: var(--paper);
  }
  .card--back {
    left: 630px;
    background: linear-gradient(160deg, var(--navy) 0%, var(--navy-deep) 100%);
    display: flex;
    align-items: center;
    justify-content: center;
  }
  .card__art {
    position: absolute;
    left: 0;
    bottom: 0;
    width: 210px;
    height: 166px;
    background: linear-gradient(90deg, var(--navy) 0%, var(--sky) 45%, var(--sky) 62%, var(--sun) 78%, var(--sun) 100%);
  }
  .wordmark {
    font-family: "Bebas Neue", sans-serif;
    font-weight: 400;
    letter-spacing: 1px;
    line-height: 1;
    display: flex;
    align-items: center;
    gap: 10px;
  }
  .wordmark__dot {
    width: 14px;
    height: 14px;
    border-radius: 50%;
    background: var(--sun);
    flex: none;
  }
  .card--front .wordmark {
    position: absolute;
    top: 50px;
    right: 36px;
    font-size: 24px;
    color: var(--navy);
  }
  .card--back .wordmark {
    font-size: 38px;
    color: #ffffff;
  }
  .contact {
    position: absolute;
    right: 36px;
    bottom: 48px;
    text-align: right;
  }
  .contact__name {
    font-family: "Bebas Neue", sans-serif;
    font-size: 24px;
    color: var(--navy);
    letter-spacing: 0.5px;
    margin: 0 0 10px;
  }
  .contact__line {
    font-family: "Open Sans", sans-serif;
    font-size: 12px;
    color: var(--ink);
    margin: 0 0 4px;
    display: flex;
    align-items: center;
    justify-content: flex-end;
    gap: 8px;
  }
  .contact__icon {
    width: 11px;
    height: 11px;
    flex: none;
  }
</style>
</head>
<body>
  <main class="sheet">
    <section class="card card--front" aria-label="Card front with contact details">
      <div class="card__art" role="img" aria-label="Large decorative window shade and setting sun artwork in blue and yellow"></div>
      <div class="wordmark"><span class="wordmark__dot"></span>Copperleaf Motorized Shade</div>
      <div class="contact">
        <p class="contact__name">Daniel Hartley</p>
        <p class="contact__line">310.555.0142
          <svg class="contact__icon" viewBox="0 0 24 24" aria-hidden="true"><path fill="#22b3ea" d="M6.6 10.8a15.1 15.1 0 0 0 6.6 6.6l2.2-2.2a1 1 0 0 1 1-.25 11.4 11.4 0 0 0 3.6.57 1 1 0 0 1 1 1V20a1 1 0 0 1-1 1A17 17 0 0 1 3 4a1 1 0 0 1 1-1h3.5a1 1 0 0 1 1 1c0 1.25.2 2.450.57 3.57a1 1 0 0 1-.25 1z"/></svg>
        </p>
        <p class="contact__line">info@copperleafshades.com
          <svg class="contact__icon" viewBox="0 0 24 24" aria-hidden="true"><rect x="2" y="5" width="20" height="14" rx="1" fill="#22b3ea"/><path d="M2 6l10 7 10-7" fill="none" stroke="#ffffff" stroke-width="1.8"/></svg>
        </p>
      </div>
    </section>
    <section class="card card--back" aria-label="Card back with company name">
      <div class="wordmark"><span class="wordmark__dot"></span>Copperleaf Motorized Shade</div>
    </section>
  </main>
</body>
</html>
```